Mentorloft needs a WordPress - Design

I am a personal, team and business coach and help my clients to develop their potential. I mainly work with individuals and teams, but this can also be in the context of a company.
My business is called "Mentorloft"

The main goal of this website is to promote my business and to attire new customers.
I also want to present my concepts and ideas about coaching and how I actually do coaching and consulting. This is also to inform potential customers what coaching actually is and what it's not.
I want to host this website on a hosting-provider and want to be able to add and adapt content on my own. I'm thus looking for a WordPress - design.

Content:

vision
• Why do I do this
• How do I do this
• What am I doing

Coaching
• Career development
• Conflicts
• What is coaching, why coaching
• Conduct of a session and of the whole consultation
Limits of coaching
• Examples of positive effects of coaching

Support concept

Blog about current topics

Left

About me

Contact form

Footer / disclaimer

The following topics are the most important parts of my daily work as a coach with my clients, maybe this helps to get choos a suitable design:
- personality development, analyzing aspects and patterns and showing their influence
- Improve collaboration and cooperation in teams
- Addressing and solving conflicts (private and business)
- Identify and foster motivation, drivers, goals and action patterns
- Define next steps for the further improvement
- Accompany reorientation in professional career
- Discovering and using the strengths of the customers

The major part of my work is direct conversation with the customer, on site or virtually. My job is to support the customer in recognizing his own ideas, goals and possibilities and to define next steps in the desired direction

Target Market(s)

Small businesses and private persons in serch of a professional coach

Industry/Entity Type

Consultant

Number of Pages Required

1 page

Font styles to use
Sans Serif

Requirements
Must have
• - Logo / Name (see attachment)
- Menu, fixed navigation
- content
- blog
- Footer (contact, disclaimer)

- I need a WordPress design suitable for Mobile and Desktop devices.
- I'm looking for a modern, friendly and easy to use web site.
- First page as Long-pager (scrolling), other pages as long-pager or standard
- Decent, friendly colors but still clear, simple
Nice to have
• - Panorama image (image changing on every load of the site)
- Quote (changing on every load of the site)

```html
<!DOCTYPE html>
<html lang="en">
<head>
<meta charset="utf-8">
<title>Mentorloft – Personal, Team and Business Coaching</title>
<link href="https://fonts.googleapis.com/css2?family=Poppins:wght@400;500;600;700&family=Open+Sans:wght@400;600;700&display=swap" rel="stylesheet">
<style>
:root{
  --blue-deep:#0d47c9;
  --blue-mid:#1f6be0;
  --blue-light:#2f9cf0;
  --cyan:#12a6ea;
  --orange:#f7a531;
  --ink:#1d1d1d;
  --text:#555;
  --muted:#777;
  --grey-band:#efefef;
  --grey-box:#f1f1f1;
  --white:#fff;
  --black:#050505;
}
*{box-sizing:border-box;margin:0;padding:0}
html,body{width:1200px;height:4128px;overflow:hidden}
body{position:relative;background:var(--white);font-family:"Open Sans",sans-serif;color:var(--text)}
.abs{position:absolute}
.head{font-family:"Poppins",sans-serif;color:var(--ink)}
.btn{position:absolute;background:var(--orange);color:var(--ink);font-family:"Poppins",sans-serif;font-weight:600;display:flex;align-items:center;justify-content:center;letter-spacing:.5px}
.photo{position:absolute}

/* hero */
.hero{position:absolute;left:0;top:0;width:1200px;height:615px;background:linear-gradient(100deg,#0b3fc0 0%,#1d62dc 45%,#2d8fee 100%);color:var(--white)}
.brand{position:absolute;left:85px;top:58px;width:140px;text-align:center}
.brand .mark{width:38px;height:38px;background:var(--white);margin:0 auto 12px}
.brand .name{font-family:"Poppins",sans-serif;font-size:15px;letter-spacing:3px;color:var(--white);font-weight:400}
.topline{position:absolute;top:46px;font-size:9px;font-weight:600;color:var(--white)}
.nav{position:absolute;top:98px;left:620px;display:flex;gap:26px;font-size:11px}
.social{position:absolute;top:95px;width:22px;height:22px;border:1px solid rgba(255,255,255,.6);border-radius:50%}
.hero .kicker{position:absolute;top:208px;width:100%;text-align:center;font-size:11px}
.hero h1{position:absolute;top:232px;width:100%;text-align:center;font-family:"Poppins",sans-serif;font-weight:700;font-size:50px;line-height:57px;color:var(--white)}
.hero .lead{position:absolute;top:356px;width:100%;text-align:center;font-size:16px;line-height:23px}
.dots{position:absolute;top:561px;left:578px;display:flex;gap:6px}
.dots span{width:8px;height:8px;border-radius:50%;background:var(--orange)}
.dots span+span{background:rgba(255,255,255,.8)}

/* vision */
.vision{position:absolute;left:85px;top:671px;width:1028px;height:175px;background:var(--grey-box);display:flex;padding-top:36px}
.vision div{flex:1;text-align:center;padding:0 30px}
.vision h3{font-family:"Poppins",sans-serif;font-size:15px;font-weight:600;color:var(--ink);margin-bottom:6px}
.vision p{font-size:12px;line-height:18.5px;color:var(--muted)}

.coaching-title{left:163px;top:890px;font-size:24px;line-height:31px;font-weight:700}
.coaching-quote{left:495px;top:893px;width:620px;font-size:12px;line-height:18px;color:var(--muted)}

.band{position:absolute;left:27px;top:1225px;width:1144px;height:316px;background:var(--grey-band)}
.card{position:absolute;top:1032px;width:325px;height:295px;overflow:hidden}
.card .photo{inset:0}
.card h4{position:absolute;left:28px;bottom:22px;font-family:"Poppins",sans-serif;font-weight:700;font-size:22px;line-height:27px;color:var(--white)}
.stat{position:absolute;top:1382px}
.stat .num{position:absolute;left:0;top:0;font-family:"Poppins",sans-serif;font-weight:700;font-size:34px;color:var(--cyan);white-space:nowrap}
.stat h5{position:absolute;left:101px;top:7px;font-family:"Poppins",sans-serif;font-size:13px;font-weight:600;color:var(--ink);white-space:nowrap}
.stat p{position:absolute;left:101px;top:40px;width:160px;font-size:14px;line-height:17px;color:var(--ink)}

/* about */
.namebox{position:absolute;left:123px;top:2153px;width:443px;height:119px;background:var(--grey-box);text-align:center}
.namebox strong{display:block;margin-top:30px;font-family:"Poppins",sans-serif;font-size:24px;color:var(--cyan);font-weight:600}
.namebox span{font-size:18px;color:var(--ink)}
.about-h{left:638px;top:1604px;font-size:25px;font-weight:600}
.about-p{left:636px;top:1654px;width:444px;font-size:12px;line-height:18.3px;color:var(--muted)}
.contact-h{left:636px;top:1905px;font-size:22px;font-weight:600}
.contact-s{left:636px;top:1941px;font-size:11.5px;color:var(--muted)}
.form{position:absolute;left:636px;top:1972px;width:439px;height:301px;background:var(--grey-box)}
.field{position:absolute;background:var(--white);font-size:11.5px;color:#888;padding:0 14px;display:flex;align-items:center}
.field.area{align-items:flex-start;padding-top:13px}

/* support */
.support{position:absolute;left:0;top:2332px;width:1200px;height:664px;background:var(--grey-band)}
.sup-kicker{left:131px;top:2390px;font-size:18px;font-weight:600;color:var(--cyan)}
.sup-h{left:127px;top:2420px;font-size:36px;font-weight:700}
.sup-p{position:absolute;left:128px;width:330px;font-size:12.3px;line-height:18.4px;color:var(--text)}
.ready{left:127px;top:2730px;font-size:22px;font-weight:600}
.rail{position:absolute;left:622px;top:2480px;width:2px;height:370px;background:#dcdcdc}
.step{position:absolute;left:596px;width:55px;height:55px;border-radius:50%;background:var(--white);display:flex;align-items:center;justify-content:center;font-family:"Poppins",sans-serif;font-weight:600;font-size:18px;color:#999;box-shadow:0 0 0 5px #f7f7f7}
.step.on{background:var(--blue-deep);color:var(--white);box-shadow:0 0 0 5px #e0e6f3}
.scard{position:absolute;left:698px;width:345px;height:157px;background:var(--white);padding:26px 30px;box-shadow:0 4px 14px rgba(0,0,0,.07);border-color:var(--white)}
.scard::before{content:"";position:absolute;left:-9px;top:60px;border:9px solid transparent;border-left:0;border-right-color:inherit}
.scard h4{font-family:"Poppins",sans-serif;font-size:19px;font-weight:600;color:#555;margin-bottom:6px}
.scard p{font-size:12px;line-height:18.4px;color:var(--muted)}
.scard.on{background:linear-gradient(100deg,var(--blue-deep),var(--cyan));border-color:var(--blue-deep);color:var(--white)}
.scard.on h4,.scard.on p{color:var(--white)}

/* blog */
.blog-h{left:0;top:3070px;width:1200px;text-align:center;font-size:36px;font-weight:600}
.post{position:absolute;top:3151px;width:277px}
.post .photo{position:relative;width:277px;height:160px}
.post h4{font-family:"Poppins",sans-serif;font-size:18px;font-weight:600;color:var(--ink);margin-top:24px}
.post small{display:block;font-size:12px;color:var(--muted);margin-top:6px}
.totop{position:absolute;left:1144px;top:3513px;width:40px;height:40px;background:var(--cyan)}

/* footer */
.footer{position:absolute;left:0;top:3568px;width:1200px;height:242px;background:var(--black);color:var(--white)}
.f-brand{position:absolute;left:195px;top:45px;width:150px;text-align:center}
.f-brand .mark{width:40px;height:40px;background:var(--white);margin:0 auto 16px}
.f-brand .name{font-family:"Poppins",sans-serif;font-size:15px;letter-spacing:3px}
.f-brand p{font-size:8.5px;line-height:11px;text-align:left;margin-top:12px;color:#ddd}
.f-item{position:absolute;left:423px;font-size:12px;line-height:17px}
.f-item small{display:block;font-size:10.5px;color:#ddd;padding-left:22px}
.f-item svg{vertical-align:-2px;margin-right:6px}
.f-links{position:absolute;left:695px;top:56px;font-size:11px;line-height:22.5px}
.f-sub{position:absolute;left:862px;top:55px;width:215px;font-size:12px;line-height:17px}
.f-input{position:absolute;left:863px;top:117px;width:224px;height:32px;background:var(--white);color:#888;font-size:11.5px;padding-left:12px;display:flex;align-items:center}
</style>
</head>
<body>

<header class="hero">
  <div class="photo" role="img" aria-label="Blue-tinted photo of a celebrating team at a laptop" style="inset:0;background:radial-gradient(ellipse at 75% 30%,rgba(120,190,255,.35),transparent 60%)"></div>
  <div class="brand"><div class="mark"></div><div class="name">MENTORLOFT</div></div>
  <div class="topline" style="left:620px">Email : info@mentorloft.com</div>
  <div class="topline" style="left:1036px">Phone : 00 44 55 66</div>
  <nav class="nav"><span>Home</span><span>Coachings</span><span>About Coach</span><span>Blog</span><span>Contact Us</span></nav>
  <span class="social" style="left:998px"></span>
  <span class="social" style="left:1029px"></span>
  <span class="social" style="left:1059px"></span>
  <span class="social" style="left:1088px"></span>
  <p class="kicker">For Individuals, Teams and Businesses</p>
  <h1>Discover the<br>Science of Sucess</h1>
  <p class="lead">Learn the cutting-edge tools to hack the productivity.<br>It works 100%. Take the action now and experience your growth.</p>
  <a class="btn" style="left:519px;top:431px;width:160px;height:38px;font-size:14px;font-weight:500">TAKE THE LEAP</a>
  <div class="dots"><span></span><span></span><span></span></div>
</header>

<section class="vision">
  <div><h3>WHY DO I DO THIS</h3><p>Sed ut perspiciatis unde omnis iste natus error sit voluptatem accusantium doloremque laudantium, totam rem aperiam, eaque ipsa quae ab illo inventore.</p></div>
  <div><h3>HOW DO I DO THIS</h3><p>Sed ut perspiciatis unde omnis iste natus error sit voluptatem accusantium doloremque laudantium, totam rem aperiam, eaque ipsa quae ab illo inventore.</p></div>
  <div><h3>WHAT I AM DOING</h3><p>Sed ut perspiciatis unde omnis iste natus error sit voluptatem accusantium doloremque laudantium, totam rem aperiam, eaque ipsa quae ab illo inventore.</p></div>
</section>

<h2 class="abs head coaching-title">COACHING<br>FOR INDVIDUAL,<br>TEAMS AND BUSINESS</h2>
<p class="abs coaching-quote">"Lorem ipsum dolor sit amet, consectetur adipiscing elit, sed do eiusmod tempor incididunt ut labore et dolore magna aliqua. Ut enim ad minim veniam, quis nostrud exercitation ullamco laboris nisi ut aliquip ex ea commodo Duis aute irure dolor in reprehenderit in voluptate velit esse cillum dolore eu fugiat nulla pariatur. Excepteur sint occaecat cupidatat non proident Duis aute irure dolor in reprehenderit in voluptate velit esse cillum dolore eu fugiat nulla pariatur.</p>

<div class="band"></div>
<svg class="abs" style="left:32px;top:1170px" width="34" height="22" viewBox="0 0 34 22"><path d="M33 11H2M11 2 2 11l9 9" fill="none" stroke="#444" stroke-width="1.6"/></svg>
<svg class="abs" style="left:1128px;top:1170px" width="34" height="22" viewBox="0 0 34 22"><path d="M1 11h31M23 2l9 9-9 9" fill="none" stroke="#444" stroke-width="1.6"/></svg>

<article class="card" style="left:85px"><div class="photo" role="img" aria-label="Photo of two people talking across a meeting table" style="background:linear-gradient(160deg,#8a9ab0,#3d4652 60%,#20252c)"></div><h4>What is Coaching,<br>Why Coaching</h4></article>
<article class="card" style="left:440px"><div class="photo" role="img" aria-label="Photo of smiling colleagues working at laptops" style="background:linear-gradient(160deg,#6b5a4a,#3a3029 55%,#1d1a18)"></div><h4>Career Development</h4></article>
<article class="card" style="left:790px"><div class="photo" role="img" aria-label="Photo of a thoughtful man in a suit by a window" style="background:linear-gradient(160deg,#b8bcc0,#5c5854 55%,#26221f)"></div><h4>Conflicts</h4></article>

<div class="stat" style="left:152px"><span class="num">500+</span><h5>HAPPY CLIENTS</h5><p>Suspendisse facilisis sem sit amet mauris posuere, ut interdum elit aliquet</p></div>
<div class="stat" style="left:466px"><span class="num">100%</span><h5>RESULT ORIENTED</h5><p>Suspendisse facilisis sem sit amet mauris posuere, ut interdum elit aliquet</p></div>
<div class="stat" style="left:783px"><span class="num">100%</span><h5>SUPPORT</h5><p>Suspendisse facilisis sem sit amet mauris posuere, ut interdum elit aliquet</p></div>

<div class="photo" role="img" aria-label="Portrait photo of the coach in a grey suit with arms crossed" style="left:130px;top:1602px;width:436px;height:551px;background:linear-gradient(180deg,#ffffff 0%,#e6e4e2 30%,#6b6864 70%,#4a4845 100%)"></div>
<div class="namebox"><strong>JOHN DOE</strong><span>Founder of Mentorloft</span></div>

<h2 class="abs head about-h">ABOUT THE COACH</h2>
<p class="abs about-p">Lorem ipsum dolor sit amet, consectetur adipisicing elit, sed do eiusmod tempor incididunt ut labore et dolore magna aliqua. Ut enim ad minim veniam, quis nostrud exercitation ullamco laboris nisi ut aliquip ex ea commodo consequat eaque ipsa quae ab illo inventore veritatis et quasi architecto beatae vitae. Curabitur sed risus quis lacus accumsan faucibus sed ut metus. Lorem ipsum dolor sit amet, consectetur adipisicing elit, sed do eiusmod tempor incididunt ut labore et dolore magna aliqua. Ut enim ad minim veniam, quis nostrud exercitation ullamco laboris nisi ut aliquip ex ea commodo consequat eaque ipsa quae ab illo inventore veritatis et quasi architecto beatae vitae. Curabitur sed risus quis lacus accumsan faucibus sed ut metus.</p>
<h3 class="abs head contact-h">Want to know more? Contact us.</h3>
<p class="abs contact-s">Fill out the form below and out team will contact you in no time.</p>
<form class="form">
  <div class="field" style="left:19px;top:21px;width:193px;height:35px">Name</div>
  <div class="field" style="left:229px;top:21px;width:189px;height:35px">Phone No.</div>
  <div class="field" style="left:19px;top:78px;width:399px;height:36px">Email ID</div>
  <div class="field area" style="left:19px;top:138px;width:399px;height:78px">Your Message</div>
  <span class="btn" style="left:19px;top:244px;width:146px;height:35px;font-size:13px">SUBMIT</span>
</form>

<section class="support"></section>
<p class="abs head sup-kicker" style="color:var(--cyan)">Sucess Starts with 3 Easy Step</p>
<h2 class="abs head sup-h">Support Concept</h2>
<p class="sup-p" style="top:2488px">Lorem ipsum dolor sit amet, consectetur adipiscing elit, sed do eiusmod tempor incididunt ut labore et dolore magna aliqua. Ut enim ad minim veniam, quis nostrud exercitation ullamco laboris nisi ut aliquip ex ea commodo consequat.</p>
<p class="sup-p" style="top:2601px">Lorem ipsum dolor sit amet, consectetur adipiscing elit, sed do eiusmod tempor incididunt ut labore et dolore magna aliqua. Ut enim ad minim veniam, quis nostrud exercitation ullamco laboris nisi ut aliquip ex ea commodo consequat.</p>
<h3 class="abs head ready">Ready to Start?</h3>
<p class="sup-p" style="top:2768px">Lorem ipsum dolor sit amet, consectetur adipiscing elit, sed do eiusmod tempor incididunt ut labore et dolore magna aliqua.</p>
<a class="btn" style="left:128px;top:2848px;width:146px;height:36px;font-size:14px;font-weight:500">Let's Talk</a>

<div class="rail"></div>
<span class="step on" style="top:2446px">01</span>
<span class="step" style="top:2632px">02</span>
<span class="step" style="top:2816px">03</span>
<div class="scard on" style="top:2397px"><h4>Make a Decision</h4><p>Lorem ipsum dolor sit amet, consectetur adipiscing elit, sed do eiusmod tempor incididunt ut labore et dolore magna aliquae lit, sed do eiusmod tempor .</p></div>
<div class="scard" style="top:2581px"><h4>Schedule a Meeting</h4><p>Lorem ipsum dolor sit amet, consectetur adipiscing elit, sed do eiusmod tempor incididunt ut labore et dolore magna aliquae lit, sed do eiusmod tempor .</p></div>
<div class="scard" style="top:2767px"><h4>Experience Transformation</h4><p>Lorem ipsum dolor sit amet, consectetur adipiscing elit, sed do eiusmod tempor incididunt ut labore et dolore magna aliquae lit, sed do eiusmod tempor .</p></div>

<h2 class="abs head blog-h">Latest from Blog</h2>
<article class="post" style="left:141px"><div class="photo" role="img" aria-label="Photo of a man with raised arms among tall buildings" style="background:linear-gradient(180deg,#c9ced4,#6d737a 60%,#2e3236)"></div><h4>Lorem Ipsum Dollar</h4><small>Jun 22, 2020 &nbsp; | &nbsp; by Anand</small></article>
<article class="post" style="left:460px"><div class="photo" role="img" aria-label="Photo of a businessman beside a chalk sketch about productivity" style="background:linear-gradient(90deg,#d9d9d9,#9a9a9a 60%,#2a2a2a)"></div><h4>Lorem Ipsum Dollar</h4><small>Jun 22, 2020 &nbsp; | &nbsp; by Anand</small></article>
<article class="post" style="left:779px"><div class="photo" role="img" aria-label="Photo of a team meeting in a bright office" style="background:linear-gradient(180deg,#c8b9a4,#8a7a68 55%,#3e4a5a)"></div><h4>Lorem Ipsum Dollar</h4><small>Jun 22, 2020 &nbsp; | &nbsp; by Anand</small></article>
<a class="btn" style="left:513px;top:3436px;width:185px;height:37px;font-size:14px;font-weight:500">EXPLORE MORE</a>

<a class="totop" aria-label="Back to top"><svg width="40" height="40" viewBox="0 0 40 40"><path d="M11 24l9-9 9 9" fill="none" stroke="#fff" stroke-width="2"/></svg></a>

<footer class="footer">
  <div class="f-brand"><div class="mark"></div><div class="name">MENTORLOFT</div><p>Etiam maximus, justo ut pellentesque egestas, erat sapien mollis massa, nec porta nisl quam eu arcu. Donec sit</p></div>
  <div class="f-item" style="top:56px"><svg width="14" height="11" viewBox="0 0 14 11"><rect x=".6" y=".6" width="12.8" height="9.8" fill="none" stroke="#fff"/><path d="M.6.6 7 6l6.4-5.4" fill="none" stroke="#fff"/></svg>Email<small>info@mentorloft.com</small></div>
  <div class="f-item" style="top:110px"><svg width="14" height="14" viewBox="0 0 14 14"><path d="M3 1l2.5 3-1.5 1.5c1 2 2.5 3.5 4.5 4.5L10 8.5l3 2.5-1.5 2C6 13 1 8 1 2.5z" fill="none" stroke="#fff"/></svg>Phone<small>00 44 55 66</small></div>
  <div class="f-item" style="top:164px"><svg width="12" height="15" viewBox="0 0 12 15"><path d="M6 14S1 8.5 1 5.5a5 5 0 0 1 10 0C11 8.5 6 14 6 14z" fill="none" stroke="#fff"/><circle cx="6" cy="5.5" r="1.8" fill="none" stroke="#fff"/></svg>Address<small>Harbor Lane 48, Westbrook</small></div>
  <nav class="f-links">About Us<br>Coaching<br>Help<br>Contact<br>Disclaimer</nav>
  <p class="f-sub">Subscribe to get the latest &nbsp;content by Mentorloft straight in your inbox.</p>
  <div class="f-input">Enter Email ID</div>
  <span class="btn" style="left:863px;top:161px;width:110px;height:31px;font-size:12px">SUBSCRIBE</span>
</footer>

</body>
</html>
```